Webdesign Metall- und Stahlbau Harkenfeld GmbH
Zielgruppe
Metall- und Stahlbau Harkenfeld GmbH
Zielgruppe: öffentlicher Bereich, Industrie, Gesundheitswesen > deutschlandweit tätig
Aufgabenstellung
keine bewegten Bilder oder Elemente in der Website
klassisches Layout
sehr konservativ

```html
<!DOCTYPE html>
<html lang="de">
<head>
<meta charset="utf-8">
<title>Metall- und Stahlbau Harkenfeld GmbH</title>
<link href="https://fonts.googleapis.com/css2?family=Open+Sans:wght@400;600&family=Roboto+Condensed:wght@400;500;700&display=swap" rel="stylesheet">
<style>
  :root {
    --navy: #1f3347;
    --navy-line: #2c4258;
    --page: #e3e3e3;
    --page-light: #ebebeb;
    --button: #7c8389;
    --text-dark: #1e1e1e;
    --text-light: #ffffff;
    --flag-black: #111111;
    --flag-red: #d21a1a;
    --flag-gold: #f2c200;
  }
  * { box-sizing: border-box; margin: 0; padding: 0; }
  html, body { width: 1200px; height: 1200px; overflow: hidden; }
  body {
    position: relative;
    background: var(--page);
    font-family: "Open Sans", Arial, sans-serif;
    color: var(--text-dark);
  }
  .site-header {
    position: absolute; left: 0; top: 41px; width: 1200px; height: 53px;
    background: var(--navy);
    border-bottom: 2px solid var(--navy-line);
  }
  .site-title {
    position: absolute; left: 168px; top: 11px;
    font-family: "Open Sans", Arial, sans-serif; font-weight: 600;
    font-size: 24px; color: var(--text-light); letter-spacing: -0.2px;
    display: flex; align-items: center; gap: 9px;
  }
  .flag { display: inline-flex; flex-direction: column; width: 26px; height: 17px; }
  .flag span { flex: 1; }
  .flag .f1 { background: var(--flag-black); }
  .flag .f2 { background: var(--flag-red); }
  .flag .f3 { background: var(--flag-gold); }
  .flag.small { width: 13px; height: 9px; }

  .main-nav {
    position: absolute; left: 0; top: 96px; width: 1200px; height: 45px;
    background: var(--navy);
  }
  .main-nav a {
    position: absolute; top: 0; height: 45px; line-height: 45px;
    font-family: "Roboto Condensed", Arial, sans-serif; font-weight: 700;
    font-size: 15px; color: var(--text-light); text-decoration: none;
    letter-spacing: 0.2px;
  }
  .main-nav a.active { background: var(--button); padding: 0 14px; }

  .hero {
    position: absolute; left: 165px; top: 164px; width: 858px; height: 400px;
    background: linear-gradient(180deg, #8a8d90 0%, #b3b5b7 45%, #6c6e70 75%, #3f4143 100%);
  }
  .hero-badge {
    position: absolute; left: 36px; bottom: 30px;
    display: flex; align-items: center; gap: 12px;
    font-family: "Roboto Condensed", Arial, sans-serif; color: var(--text-light);
  }
  .hero-badge .brand { font-weight: 700; font-size: 17px; }
  .hero-badge .tagline { font-size: 12px; display: flex; align-items: center; gap: 5px; }

  .welcome {
    position: absolute; left: 165px; top: 588px; width: 298px; height: 282px;
    background: var(--navy); color: var(--text-light);
    padding: 44px 22px 0 22px;
  }
  .welcome h2 {
    font-family: "Roboto Condensed", Arial, sans-serif; font-weight: 700;
    font-size: 29px; letter-spacing: 0.3px; margin-bottom: 14px;
  }
  .welcome p { font-size: 14px; line-height: 20px; }
  .button {
    display: inline-block; background: var(--button); color: var(--text-light);
    font-family: "Roboto Condensed", Arial, sans-serif; font-weight: 500;
    font-size: 13.5px; padding: 0 11px; height: 32px; line-height: 32px;
    text-decoration: none;
  }
  .welcome .button { position: absolute; left: 21px; top: 238px; }

  .photo { position: absolute; }
  .photo-welding { left: 485px; top: 588px; width: 136px; height: 201px;
    background: linear-gradient(160deg, #4a4c4f 0%, #7d8084 50%, #2f3133 100%); }
  .photo-hall { left: 629px; top: 588px; width: 140px; height: 201px;
    background: linear-gradient(180deg, #a7a9ab 0%, #6d6f72 55%, #3c3e40 100%); }
  .photo-bridge { left: 791px; top: 588px; width: 252px; height: 180px;
    background: linear-gradient(180deg, #c9cacb 0%, #9fa1a3 60%, #8a8c8e 100%); }

  .section-heading {
    position: absolute;
    font-family: "Roboto Condensed", Arial, sans-serif; font-weight: 500;
    font-size: 21px; color: var(--text-dark);
  }
  .services-heading { left: 491px; top: 810px; }
  .service-list {
    position: absolute; left: 512px; top: 860px; list-style: disc;
    font-size: 14.5px; line-height: 21.5px; padding-left: 0;
  }
  .news-heading { left: 791px; top: 789px; }
  .news-list {
    position: absolute; left: 791px; top: 846px; list-style: none;
    font-size: 12px; line-height: 20px; letter-spacing: -0.2px;
  }
  .news-button { position: absolute; left: 791px; top: 902px; }

  .site-footer {
    position: absolute; left: 0; top: 1104px; width: 1200px; height: 43px;
    background: var(--navy);
  }
  .site-footer a {
    position: absolute; top: 0; line-height: 43px;
    font-family: "Roboto Condensed", Arial, sans-serif; font-weight: 500;
    font-size: 14.5px; color: var(--text-light); text-decoration: none;
  }
</style>
</head>
<body>
  <header class="site-header">
    <div class="site-title">Metall- und Stahlbau Harkenfeld GmbH
      <span class="flag" aria-hidden="true"><span class="f1"></span><span class="f2"></span><span class="f3"></span></span>
    </div>
  </header>

  <nav class="main-nav">
    <a class="active" href="#" style="left:165px">HOME</a>
    <a href="#" style="left:254px">LEISTUNGEN</a>
    <a href="#" style="left:357px">REFERENZEN</a>
    <a href="#" style="left:457px">STELLENANGEBOTE</a>
    <a href="#" style="left:595px">AKTUELLE MELDUNGEN</a>
    <a href="#" style="left:755px">DOWNLOAD</a>
    <a href="#" style="left:856px">UNTERNEHMENSVORSTELLUNG</a>
  </nav>

  <section class="hero" role="img" aria-label="Schwarzweißfoto einer Stahlbaustelle mit Kran, Stahlträgern und Monteuren unter bewölktem Himmel">
    <div class="hero-badge">
      <span class="brand">Harkenfeld</span>
      <span class="tagline">TRADITION SEIT 1965.
        <span class="flag small" aria-hidden="true"><span class="f1"></span><span class="f2"></span><span class="f3"></span></span>
      </span>
    </div>
  </section>

  <section class="welcome">
    <h2>WILLKOMMEN</h2>
    <p>Metall- und Stahlbau Harkenfeld GmbH ist Ihr zuverlässiger Partner für komplexe Metall- und Stahlkonstruktionen. Als etabliertes Meisterunternehmen stehen wir seit 1965 für Qualität, Präzision und technische Kompetenz.</p>
    <a class="button" href="#">MEHR ÜBER UNS</a>
  </section>

  <div class="photo photo-welding" role="img" aria-label="Schweißer bei der Arbeit mit Funkenflug"></div>
  <div class="photo photo-hall" role="img" aria-label="Fertigungshalle mit Stahlträgern"></div>
  <h3 class="section-heading services-heading">UNSERE LEISTUNGEN</h3>
  <ul class="service-list">
    <li>Stahlkonstruktionen</li>
    <li>Industriemontage</li>
    <li>Brückenbau</li>
    <li>Sonderanfertigungen</li>
  </ul>

  <div class="photo photo-bridge" role="img" aria-label="Stählerne Bogenbrücke über einem Fluss"></div>
  <h3 class="section-heading news-heading">AKTUELLES</h3>
  <ul class="news-list">
    <li>31.01.2026: Großauftrag für neue Klinikgebäude erhalten.</li>
    <li>15.12.2025: Zertifizierung nach DIN EN 1090-1 erneuert.</li>
  </ul>
  <a class="button news-button" href="#">ALLE MELDUNGEN</a>

  <footer class="site-footer">
    <a href="#" style="left:173px">IMPRESSUM</a>
    <a href="#" style="left:301px">DATENSCHUTZ</a>
    <a href="#" style="left:445px">BFSG</a>
    <a href="#" style="left:531px">KONTAKT</a>
  </footer>
</body>
</html>
```